new website screendesign for real estate company

We need new website design
The design must fit into the Corporate Identity design of the company.

old page
http://www.wohnkarta.at/

we made some layout.png where you can see the components
http://93.12.204.17:8080/Layout.png
+ its attached

dont design exactly like this we just copied different things together. you can design anything new

the layout.png should just show you the direction. and you can see the basic structure of the page

upper left logo upper right login
navigation
banner slider
search filter

carousel with top objects (real estate)

the lower 4 points are predefined search results. for example when "für Anspruchsvolle" is clicked all luxury objects are displayed
when "WG geeignet" is clicked it shows objects for low budget and students.

also find fitting images for all the once used in layout.png are quite bad

here are some of our previous real estate projects

http://93.12.88.6:8082/brelt/
http://www.quirba.at/
http://www.lerchen-immobilien.at/

```html
<!DOCTYPE html>
<html lang="de">
<head>
<meta charset="utf-8">
<title>Wohnkarta – Immobilien</title>
<link rel="stylesheet" href="https://fonts.googleapis.com/css2?family=Open+Sans:wght@400;600;700&family=Oswald:wght@400;500&family=Lato:wght@400;700&display=swap">
<style>
:root{
  --orange:#f6a650;
  --orange-dark:#e88c2c;
  --nav-active:#d9471f;
  --teal:#1fb3ac;
  --red:#e2262b;
  --brown:#b0773a;
  --brown-line:#d6ad80;
  --ink:#444;
  --muted:#777;
  --white:#fff;
  --bar:#4a4a4a;
}
*{box-sizing:border-box;margin:0;padding:0}
html,body{width:908px;height:1200px;overflow:hidden}
body{position:relative;background:var(--white);font-family:'Open Sans',sans-serif;color:var(--ink)}
.abs{position:absolute}

/* top bar */
.topbar{left:0;top:0;width:908px;height:35px;border-top:3px solid var(--orange);background:var(--white);border-bottom:1px solid #e4e4e4}
.topbar .cell{position:absolute;top:0;height:32px;display:flex;align-items:center;font-size:9px;border-right:1px solid #e6e6e6}
.lang{left:56px;width:132px;padding-left:14px;border-left:1px solid #e6e6e6}
.lang .flag{width:10px;height:7px;background:#3a4e8c;margin-right:9px}
.lang b{font-weight:600;color:#333}
.lang .caret{margin-left:auto;margin-right:14px;color:#aaa;font-size:8px}
.company{left:188px;width:370px;padding-left:30px;border-right:none}
.company .badge{width:16px;height:16px;border-radius:50%;background:#e8b23a;margin-right:16px}
.company span{color:#2f7fb5;font-weight:700;font-size:10.5px}
.account{left:566px;width:124px;justify-content:center;gap:6px;border-left:1px solid #e6e6e6}
.account .signin{font-weight:700;color:#333}
.account .or{color:#999}
.account .join{border:1px solid #ccc;padding:2px 6px;font-weight:700;color:#333}
.search-top{left:690px;width:170px;padding-left:14px;color:#bbb}
.search-top svg{margin-left:auto;margin-right:12px}

/* header */
.header{left:0;top:35px;width:908px;height:70px;background:var(--orange);border-bottom:1px solid #d98b3a}
.logo{left:84px;top:14px;display:flex;align-items:center;gap:6px}
.logo .mark{width:14px;height:14px;background:var(--nav-active)}
.logo span{font-size:15px;font-weight:700;color:var(--white);letter-spacing:.5px}
.nav{right:60px;top:0;height:70px;display:flex;gap:0}
.nav a{display:block;padding:0 14px;line-height:73px;font-size:10px;font-weight:600;letter-spacing:1.3px;color:var(--white);text-decoration:none;text-transform:uppercase}
.nav a.active{color:var(--nav-active);border-bottom:3px solid var(--nav-active);line-height:70px}

/* hero */
.hero{left:0;top:105px;width:908px;height:299px;background:linear-gradient(100deg,#6b4c34 0%,#a58163 22%,#d8d2c8 45%,#e9e6e1 62%,#9c8067 82%,#5d4432 100%)}
.hero-caption{left:365px;top:195px;width:372px;height:143px;background:rgba(255,255,255,.55)}
.hero-caption h1{position:absolute;left:30px;top:18px;font-family:'Oswald',sans-serif;font-weight:400;font-size:23px;color:var(--orange-dark)}
.hero-caption p{position:absolute;left:34px;top:56px;width:310px;font-size:10px;line-height:15px;color:#444}
.hero-caption .more{position:absolute;left:276px;top:104px;font-size:9px;font-weight:700;color:var(--teal);letter-spacing:.3px}
.price{left:394px;top:298px}
.arrow{width:26px;height:26px;border-radius:50%;background:var(--white);display:flex;align-items:center;justify-content:center}

/* search filter */
.filter{left:0;top:404px;width:908px;height:53px;background:var(--bar)}
.field{position:absolute;top:15px;height:24px;background:var(--white);font-size:9px;color:#999;display:flex;align-items:center;padding-left:10px}
.field .cur{color:#555;width:22px;border-right:1px solid #ddd;height:100%;display:flex;align-items:center;margin-right:10px}
.field .tri{margin-left:8px;border:3px solid transparent;border-top:4px solid #888;margin-top:3px}
.radios{left:675px;top:16px;font-size:7.5px;color:#ddd;line-height:12px}
.radios i{display:inline-block;width:6px;height:6px;border-radius:50%;border:1px solid #bbb;margin-right:6px}
.radios i.on{background:#8ec63f;border-color:#8ec63f}
.btn-search{left:730px;top:15px;width:106px;height:24px;background:var(--teal);color:var(--white);font-size:9.5px;display:flex;align-items:center;justify-content:center}

/* top objects */
.section-title{left:0;top:526px;width:908px;text-align:center;font-size:18px;color:#555;letter-spacing:.4px}
.card{position:absolute;top:595px;width:196px}
.card .photo{width:196px;height:131px;border:2px solid #ddd;position:relative}
.card .tag{position:absolute;right:0;top:14px;background:var(--red);color:var(--white);font-size:10px;font-weight:600;padding:6px 9px}
.card p{margin-top:11px;font-size:8.2px;line-height:13px;color:#777;text-align:justify}
.card .btn{position:absolute;top:202px;width:86px;height:25px;background:var(--orange);color:var(--white);font-size:6px;font-weight:700;display:flex;align-items:center;justify-content:center}
.chev{top:656px}

/* footer */
.footer{left:0;top:873px;width:908px;height:327px;background:var(--brown);color:var(--white);font-family:'Lato',sans-serif}
.col{position:absolute;top:56px}
.col h3{font-size:12.5px;font-weight:700;letter-spacing:.2px;margin-bottom:19px}
.col li{list-style:none;font-size:10px;line-height:18px}
.newsletter input{display:block;width:116px;height:19px;border:none;background:var(--white);font-family:inherit;font-size:10px;color:#e9a57a;text-align:center;margin-bottom:5px}
.newsletter .submit{width:116px;height:31px;background:#222;color:var(--white);font-size:11px;font-weight:700;display:flex;align-items:center;justify-content:center}
.share{position:absolute;top:222px;left:445px;display:flex;gap:5px;font-size:8px;font-weight:700}
.share span{background:#4d65a0;padding:1px 5px}
.share em{font-style:normal;background:var(--white);color:#333;padding:1px 3px;font-weight:400}
.contact p{font-size:9.8px;line-height:13.5px;color:#fbe9d6}
.contact .strong{font-weight:700;color:var(--white);line-height:18px}
.socials{display:flex;gap:6px;margin-top:8px}
.socials span{width:27px;height:27px;border-radius:4px;background:#e9d6c0}
.footer-line{left:84px;top:1147px;width:737px;height:1px;background:var(--brown-line)}
.copyright{left:102px;top:1162px;font-family:'Lato',sans-serif;font-size:9.5px;font-weight:700;color:var(--white)}
</style>
</head>
<body>

<div class="abs topbar">
  <div class="cell lang"><span class="flag"></span><b>English</b><span class="caret">&#9662;</span></div>
  <div class="cell company"><span class="badge"></span><span>Dr. Halbinger Immobilien GmbH</span></div>
  <div class="cell account"><span class="signin">Sign in</span><span class="or">or</span><span class="join">Join now</span></div>
  <div class="cell search-top">Search...
    <svg width="11" height="11" viewBox="0 0 11 11"><circle cx="4.5" cy="4.5" r="3.5" fill="none" stroke="#aaa" stroke-width="1.3"/><line x1="7" y1="7" x2="10" y2="10" stroke="#aaa" stroke-width="1.5"/></svg>
  </div>
</div>

<header class="abs header">
  <div class="abs logo" style="top:26px"><span class="mark"></span><span>Wohnkarta</span></div>
  <nav class="abs nav">
    <a class="active">Immobiliensuche</a>
    <a>Suchauftrag</a>
    <a>Fur Eigentumer</a>
    <a>Team</a>
    <a>Service</a>
    <a>Contact</a>
  </nav>
</header>

<div class="abs hero" role="img" aria-label="Photo of a bright open-plan loft with bedroom, glass staircase and dining table"></div>
<div class="abs arrow" style="left:125px;top:264px"><svg width="10" height="10" viewBox="0 0 10 10"><path d="M6.5 1.5 3 5l3.5 3.5" fill="none" stroke="#333" stroke-width="1.8"/></svg></div>
<div class="abs arrow" style="left:768px;top:264px"><svg width="10" height="10" viewBox="0 0 10 10"><path d="M3.5 1.5 7 5 3.5 8.5" fill="none" stroke="#333" stroke-width="1.8"/></svg></div>
<div class="abs hero-caption">
  <h1>480 Marisol Avenue, Harbor Gables</h1>
  <p>Lorem Ipsum is simply dummy text of the printing and typesetting industry</p>
  <span class="more">READ MORE--&gt;</span>
</div>
<svg class="abs price" width="86" height="44" viewBox="0 0 86 44">
  <polygon points="0,12 43,0 86,12 86,44 0,44" fill="#1fb3ac"/>
  <text x="43" y="33" text-anchor="middle" font-family="Open Sans, sans-serif" font-weight="700" font-size="13" fill="#fff">$ 625,000</text>
</svg>

<div class="abs filter">
  <div class="field" style="left:82px;width:124px">City</div>
  <div class="field" style="left:215px;width:69px">Category<span class="tri"></span></div>
  <div class="field" style="left:294px;width:52px">Type<span class="tri"></span></div>
  <div class="field" style="left:356px;width:145px"><span class="cur">$</span>Min price</div>
  <div class="field" style="left:511px;width:145px"><span class="cur">$</span>Max price</div>
  <div class="abs radios"><div><i class="on"></i>Kauf</div><div><i></i>Miete</div></div>
  <div class="abs btn-search">Search</div>
</div>

<h2 class="abs section-title" style="font-weight:400">TOP OBJEKTE DES MONATAS</h2>

<svg class="abs chev" style="left:66px" width="12" height="20" viewBox="0 0 12 20"><path d="M10 1 2 10l8 9" fill="none" stroke="#bbb" stroke-width="1.3"/></svg>
<svg class="abs chev" style="left:826px" width="12" height="20" viewBox="0 0 12 20"><path d="M2 1l8 9-8 9" fill="none" stroke="#bbb" stroke-width="1.3"/></svg>

<div class="card" style="left:109px">
  <div class="photo" role="img" aria-label="Photo of a grey two-storey family house with lawn" style="background:linear-gradient(#9db8d6 0%,#c9d2da 45%,#6b6a66 70%,#4f8a3a 100%)"><span class="tag">$ 359.00</span></div>
  <p>Lorem Ipsum is simply dummy text of the printing and typesetting industry. Lorem Ipsum has been the industry's standard dummy text ever.</p>
  <div class="btn">READ MORE</div>
</div>
<div class="card" style="left:355px">
  <div class="photo" role="img" aria-label="Photo of a cream colonial house among green trees" style="background:linear-gradient(#6f9fd6 0%,#3f6f3a 40%,#d9d2ae 65%,#5b9a3e 100%)"><span class="tag">$ 359.00</span></div>
  <p>Lorem Ipsum is simply dummy text of the printing and typesetting industry. Lorem Ipsum has been the industry's standard dummy text ever.</p>
  <div class="btn">READ MORE</div>
</div>
<div class="card" style="left:600px">
  <div class="photo" role="img" aria-label="Photo of a white villa with blue roofs and a driveway" style="background:linear-gradient(#4f8fd9 0%,#dfe6ee 45%,#9aa6b3 75%,#6d8a52 100%)"><span class="tag">$ 359.00</span></div>
  <p>Lorem Ipsum is simply dummy text of the printing and typesetting industry. Lorem Ipsum has been the industry's standard dummy text ever.</p>
  <div class="btn">READ MORE</div>
</div>

<footer class="abs footer">
  <div class="col" style="left:100px">
    <h3>SITE MAP</h3>
    <ul><li>Immobilsien</li><li>Service</li><li>Team</li><li>Impressum</li><li>Suchauftag</li><li>Vermiter</li></ul>
  </div>
  <div class="col" style="left:275px">
    <h3>NAVIGATIONS</h3>
    <ul><li>Immobilsien</li><li>Service</li><li>Team</li><li>Impressum</li><li>Suchauftag</li><li>Vermiter</li></ul>
  </div>
  <div class="col newsletter" style="left:448px">
    <h3>SIGN NEWSLETTER</h3>
    <input type="text" value="Your Name" readonly>
    <input type="text" value="Your Email" readonly>
    <div class="submit">SUBMIT</div>
  </div>
  <div class="share"><span>Gefällt mir</span><span>Teilen</span><em>53</em></div>
  <div class="col contact" style="left:646px">
    <h3 style="margin-bottom:10px">KONTAKT</h3>
    <p>DR. HALBINGER IMMOBILIEN GMBH<br>Berhordlich konzessionerter<br>Immobilienmakker</p>
    <p style="margin-top:18px">A- 1030 Wien,Lindengasse 12</p>
    <p class="strong" style="margin-top:4px">TEL: + 431 / 562 30 17<br>FAX: + 431 / 562 30 17-90</p>
    <p style="margin-top:8px">office@wohnkarta.at</p>
    <div class="socials"><span></span><span></span><span></span></div>
  </div>
</footer>
<div class="abs footer-line"></div>
<div class="abs copyright">© 2015.wohnkarta.All rights reserved</div>

</body>
</html>
```